Adventure and fiction Brazilian Rainforest Secrets book called Hollow Tide*

I want the reader to be curious about the cover. I want the cover to make you want to see the contents of the book. Both physical and digital on shelves or on websites. Eye-grabbing and eye-popping. Something that would make me abandon anything I was doing to go to the shelf and flip through the book.

I'd like a bright and live green cover. With rainforest. With small human figure in the middle of the forest.

If possible, use image composition IOI as per attachment.

Please hide a camouflaged UFO for internal joke.

Note: The name of the book in Portuguese is Maré Oca (Hollow Tide).

Note 2: The book is set on an island in the Atlantic Ocean. If you want you can include beaches, sea and hills in the distance.

Note 3: The book is not for children.

Target Market(s)

Corvalo glint, E-book, Websites, libraries

Requirements
Must have
• Something that would make me abandon anything I was doing to go to the shelf and flip through the book.
Nice to have
• Small human figure in the middle of the rainforest.
• Bright and live Green cover (If you got any new ideas of colors to stand out, please go ahead.)
• Hidden camouflaged UFO for internal joke
• Composition IOI
• Beaches, sea and hills in the distance
• Something attractive. Irresistible.
Should not have
• It's not a children's book - Please no kids themes

```html
<!DOCTYPE html>
<html lang="pt">
<head>
<meta charset="utf-8">
<title>Maré Oca — Cover Spread</title>
<link rel="stylesheet" href="https://fonts.googleapis.com/css2?family=Rubik+Distressed&family=Marcellus&family=Didact+Gothic&display=swap">
<style>
  :root {
    --page-bg: #c9d1d0;
    --teal-deep: #12302d;
    --teal-mid: #1f5a55;
    --teal-glow: #8fd3cc;
    --teal-dark: #0c2220;
    --ink-light: #f3f6f5;
    --ink-soft: #e2ecea;
  }
  * { box-sizing: border-box; margin: 0; padding: 0; }
  html, body {
    width: 1200px;
    height: 800px;
    overflow: hidden;
    background: var(--page-bg);
  }
  .spread {
    position: relative;
    width: 1200px;
    height: 800px;
  }
  .forest-photo {
    position: absolute;
    inset: 0;
    background:
      radial-gradient(ellipse 55% 45% at 22% 72%, var(--teal-glow) 0%, rgba(110,190,182,0.55) 35%, rgba(31,90,85,0) 75%),
      linear-gradient(180deg, var(--teal-mid) 0%, #1a4a46 45%, var(--teal-deep) 88%, var(--teal-dark) 100%);
  }
  .front-cover {
    position: absolute;
    left: 180px;
    top: 90px;
    width: 380px;
    height: 620px;
    overflow: hidden;
    box-shadow: 0 14px 30px rgba(0,0,0,0.25);
  }
  .cover-title {
    position: absolute;
    left: 0;
    right: 0;
    top: 92px;
    text-align: center;
    font-family: "Rubik Distressed", "Impact", sans-serif;
    font-size: 92px;
    line-height: 0.98;
    color: var(--ink-light);
    letter-spacing: 1px;
  }
  .cover-author {
    position: absolute;
    left: 0;
    right: 0;
    top: 318px;
    text-align: center;
    font-family: "Marcellus", "Georgia", serif;
    font-size: 25px;
    letter-spacing: 3px;
    color: var(--ink-light);
  }
  .back-cover {
    position: absolute;
    left: 640px;
    top: 100px;
    width: 340px;
    height: 600px;
    overflow: hidden;
    box-shadow: 0 14px 30px rgba(0,0,0,0.25);
  }
  .back-cover .forest-photo {
    background:
      radial-gradient(ellipse 60% 40% at 40% 70%, rgba(70,140,132,0.6) 0%, rgba(31,90,85,0) 70%),
      linear-gradient(180deg, var(--teal-mid) 0%, #1b4642 50%, var(--teal-deep) 100%);
  }
  .blurb {
    position: absolute;
    left: 10px;
    right: 14px;
    font-family: "Didact Gothic", "Century Gothic", sans-serif;
    font-size: 10.4px;
    line-height: 1.33;
    color: var(--ink-soft);
  }
  .blurb--lead { top: 50px; }
  .blurb--second { top: 304px; }
  .blurb--closing { top: 430px; left: 58px; }
  .spine {
    position: absolute;
    left: 980px;
    top: 100px;
    width: 40px;
    height: 600px;
    overflow: hidden;
    box-shadow: 0 14px 30px rgba(0,0,0,0.25);
  }
  .spine .forest-photo {
    background: linear-gradient(180deg, var(--teal-mid) 0%, #1a4541 55%, var(--teal-deep) 100%);
  }
  .spine-title,
  .spine-author {
    position: absolute;
    left: 50%;
    writing-mode: vertical-rl;
    transform: translateX(-50%);
    color: var(--ink-light);
    white-space: nowrap;
  }
  .spine-title {
    top: 58px;
    font-family: "Rubik Distressed", "Impact", sans-serif;
    font-size: 21px;
    letter-spacing: 1px;
  }
  .spine-author {
    top: 420px;
    font-family: "Marcellus", "Georgia", serif;
    font-size: 10px;
    letter-spacing: 2px;
  }
</style>
</head>
<body>
<main class="spread">

  <section class="front-cover">
    <div class="forest-photo" role="img" aria-label="Misty teal forest with tall dark trees and a glowing light, a lone human silhouette standing small at the lower left"></div>
    <h1 class="cover-title">MARÉ<br>OCA</h1>
    <p class="cover-author">AUTHOR NAME</p>
  </section>

  <section class="back-cover">
    <div class="forest-photo" role="img" aria-label="Dark misty teal forest continuing across the back cover"></div>
    <p class="blurb blurb--lead">Lorem ipsum dolor sit amet, consectetur adipiscing elit, sed do eiusmod tempor incididunt ut labore et dolore magna aliqua. Pellentesque massa placerat duis ultricies lacus sed turpis. Mattis aliquam faucibus purus in massa. Volutpat ac tincidunt vitae semper. Dictum at tempor commodo ullamcorper a lacus vestibulum sed arcu. Posuere sollicitudin aliquam ultrices sagittis. Dui sapien eget mi proin sed libero enim. Egestas sed tempus urna et pharetra pharetra massa. Ornare quam viverra orci sagittis eu volutpat. Suspendisse ultrices gravida dictum fusce ut placerat. Tempus iaculis urna id volutpat lacus laoreet. Sed lectus vestibulum mattis ullamcorper velit sed ullamcorper. Interdum velit laoreet id donec. Odio eu feugiat pretium nibh ipsum consequat. Velit dignissim sodales ut eu sem integer vitae justo eget. Nibh tortor id aliquet lectus proin nibh nisl condimentum id. Pharetra sit amet aliquam id diam maecenas ultricies. Ac placerat vestibulum lectus mauris ultrices eros.</p>
    <p class="blurb blurb--second">Sed vulputate odio ut enim blandit volutpat maecenas. Ac tincidunt vitae semper quis lectus nulla at volutpat. Ut diam quam nulla porttitor massa id neque aliquam. Suscipit adipiscing bibendum est ultricies integer quis auctor. Senectus et netus et malesuada fames ac turpis egestas. Tortor dignissim convallis aenean et tortor at risus. Turpis egestas sed tempus urna et pharetra pharetra massa massa. Fusce ut placerat orci nulla pellentesque. Adipiscing elit duis tristique sollicitudin.</p>
    <p class="blurb blurb--closing">Mattis enim ut tellus elementum sagittis vitae et leo. Ut sem nulla pharetra diam sit amet nisl. Urna nunc id cursus metus aliquam eleifend mi in nulla. Mi sit amet mauris commodo quis. Mus mauris vitae ultricies leo integer malesuada. Pulvinar etiam non quam lacus suspendisse faucibus interdum posuere.</p>
  </section>

  <aside class="spine">
    <div class="forest-photo" role="img" aria-label="Teal forest texture on the spine"></div>
    <span class="spine-title">MARÉ OCA</span>
    <span class="spine-author">AUTHOR NAME</span>
  </aside>

</main>
</body>
</html>
```